Sunlit Path Society the biggest community for CarbonOffset in the travel industry

We are a platform building a community for people to be able to measure and compensate carbon footprint. This community will be focused on Individuals and Businesses where they can measure their impact and choose projects to offset. I want to have a calculator of the number of kms being compensated as a community as well as the number of tons being removed. We are building the biggest community in the travel industry where users of Tours, Car Rentals, Events and eventually hotels will measure their footprint and contribute to a project to compensate and become part of the community to learn, connect and help with the environment. We will also invite companies to be part of the project so that they can offer this to their clients and employees.

Target Market(s)

At first travelers on holidays, business, events, conferences, tour operators. Next phase rental car companies, ride sharing apps

Industry/Entity Type

Travel

Number of Pages Required

1 page

Font styles to use
Serif
Sans Serif

Colors

Designer to choose colors to be used in the design.

Requirements
Must have
• A lot of images with an optimist focus. I want to stop the message that we are doomed and change it to we have an opportunity to do something, celebrate about that and build a community around this. It is intended for people between 25 - 50 years old. I want this project to be more human, our interaction and need to connect with nature. How it benefits us, etc.
Nice to have
• Videos of the projects, videos of people from the community sharing their thoughts. I am imagining somewhere within the webpage to have a mosaic with the pictures (from facebook if authorised by each person) to get and idea of how big the community is and put a human face.
Should not have
• Blaming messages of how the world will end, we have enough information on that.

```html
<!DOCTYPE html>
<html lang="en">
<head>
<meta charset="utf-8">
<title>Sunlit Path Society</title>
<link href="https://fonts.googleapis.com/css2?family=Lato:wght@400;700&family=Nunito:wght@700;800&display=swap" rel="stylesheet">
<style>
:root{
  --green-dark:#4d6b4c;
  --green-light:#79c69a;
  --green-pale:#a9dcbf;
  --ink:#333333;
  --muted:#555555;
  --footer:#4a4a4a;
  --white:#ffffff;
}
*{box-sizing:border-box;margin:0;padding:0}
html,body{width:1200px;height:3620px;overflow:hidden}
body{position:relative;background:var(--white);font-family:"Lato",sans-serif;color:var(--ink)}
.abs{position:absolute}
.heading{font-family:"Nunito",sans-serif;font-weight:800;letter-spacing:.5px}
.btn{position:absolute;display:flex;align-items:center;justify-content:center;border-radius:20px;color:var(--white);font-size:14px;background:var(--green-dark)}
.btn.light{background:var(--green-light)}

/* header */
.menu-icon{left:82px;top:46px;width:24px}
.menu-icon span{display:block;height:3px;background:#222;margin-bottom:6px;border-radius:2px}
.brand{left:0;width:1200px;top:38px;display:flex;justify-content:center;align-items:center;gap:10px}
.brand-dot{width:40px;height:40px;border-radius:50%;background:var(--green-dark)}
.brand-name{font-family:"Lato",sans-serif;font-weight:700;font-size:26px;color:var(--green-dark)}
.call{left:980px;top:44px;display:flex;gap:10px;align-items:center;font-size:12px;line-height:16px}
.call b{color:var(--green-dark);font-weight:400}

/* hero */
.hero{left:0;top:125px;width:1200px;height:572px}
.hero-title{left:125px;top:318px;font-size:33px;line-height:38px;color:var(--green-dark)}
.hero-text{left:127px;top:407px;width:320px;font-size:12.5px;line-height:16px;color:var(--muted)}
.video{left:600px;top:225px;width:520px;height:362px;border-radius:8px;background:linear-gradient(135deg,#8a9aa8,#c9b8a6 55%,#6f7f8c);box-shadow:0 12px 28px rgba(0,0,0,.35)}
.video-bar{left:630px;top:537px;width:462px;height:3px;background:var(--white)}
.video-knob{left:622px;top:530px;width:16px;height:16px;border-radius:50%;background:var(--white)}

/* steps */
.step{position:absolute;top:765px;width:200px;text-align:center}
.step-circle{width:180px;height:180px;margin:0 auto;border-radius:50%;background:var(--green-light);display:flex;align-items:center;justify-content:center}
.step-circle.active{background:var(--green-dark)}
.step h3{margin-top:24px;font-family:"Nunito",sans-serif;font-size:20px;font-weight:700;color:#444}
.step p{margin-top:24px;font-size:11px;line-height:15px;color:var(--muted);padding:0 12px}

/* projects */
.project{position:absolute;top:1156px;width:323px;text-align:center}
.project-photo{height:323px}
.project h3{margin-top:22px;font-family:"Nunito",sans-serif;font-size:26px;font-weight:700;color:#444}
.project p{margin-top:14px;font-size:14px;line-height:18px;color:var(--muted);padding:0 14px}
.project .btn{position:relative;width:177px;height:40px;margin:30px auto 0}

/* offset banner */
.offset{left:0;top:1757px;width:1200px;height:453px}
.offset-box{left:124px;top:1815px;width:428px;height:333px;background:var(--green-dark);color:var(--white);text-align:center;padding-top:36px}
.offset-box h2{font-family:"Nunito",sans-serif;font-size:25px;line-height:31px;font-weight:700}
.offset-box p{margin:28px auto 0;width:300px;font-size:13.5px;line-height:17px}
.counter{margin-top:20px;display:flex;justify-content:center;align-items:center;gap:6px;font-size:28px}
.digit{width:24px;height:34px;border:1.5px solid var(--white);display:flex;align-items:center;justify-content:center;font-size:27px}
.group{display:flex;gap:2px;margin-right:8px}
.offset-box .btn{position:relative;width:177px;height:38px;margin:22px auto 0;font-size:13px}

/* news */
.news-title{left:0;width:1200px;top:2268px;text-align:center;font-size:32px;color:#333}
.news-card{position:absolute;top:2328px;width:342px;height:360px;background:var(--white);box-shadow:0 2px 8px rgba(0,0,0,.12);padding:10px 12px}
.news-photo{height:198px}
.news-date{position:absolute;left:30px;top:175px;width:38px;height:46px;background:var(--green-light);color:var(--white);font-size:11px;font-weight:700;text-align:center;line-height:14px;padding-top:8px}
.news-card h4{margin:42px 16px 0;font-size:12.5px;letter-spacing:.5px}
.news-card p{margin:8px 16px 0;font-size:12px;line-height:15px;color:var(--muted)}
.news-card a{display:inline-block;margin:12px 16px 0;font-size:13px;color:var(--ink)}

/* benefits */
.benefit-block{left:80px;top:2793px;width:458px;height:340px;background:var(--green-light)}
.benefit-photo{left:98px;top:2811px;width:472px;height:337px}
.benefit-title{left:617px;top:2830px;font-size:33px;color:var(--green-dark)}
.benefit-rule{left:617px;top:2885px;width:85px;height:2px;background:var(--green-light)}
.benefit-text{left:617px;top:2908px;width:505px;font-size:12.5px;line-height:19px;color:var(--muted)}
.checks{left:620px;top:3004px;font-size:13px;color:var(--muted);list-style:none}
.checks li{display:flex;align-items:center;gap:8px;height:26px}

/* footer */
.footer{left:0;top:3282px;width:1200px;height:275px}
.footer-brand{left:110px;top:3375px;display:flex;align-items:center;gap:10px}
.footer-brand .brand-name{color:var(--white);font-size:22px}
.footer-brand .brand-dot{background:var(--white)}
.socials{left:120px;top:3458px;display:flex;gap:14px}
.social{width:32px;height:32px;border-radius:50%;border:2px solid var(--white)}
.social.on{background:var(--green-light);border-color:var(--green-light)}
.contact-title{left:0;width:1200px;top:3312px;text-align:center;color:var(--white);font-weight:700;font-size:15px}
.contact-rule{left:577px;top:3345px;width:46px;height:2px;background:var(--white)}
.field{position:absolute;border:1px solid #cfcfcf;color:var(--white);font-size:12px;padding:6px 8px;height:32px}
.quick{left:933px;top:3340px;color:var(--white)}
.quick h5{font-size:15px}
.quick-rule{width:96px;height:2px;background:var(--white);margin:8px 0 14px}
.quick li{list-style:none;display:flex;gap:14px;font-size:12.5px;line-height:24px}
.quick li span.ic{width:16px}
.copyright{left:0;width:1200px;top:3573px;text-align:center;font-size:13.5px;color:#444}
</style>
</head>
<body>

<header>
  <div class="abs menu-icon"><span></span><span></span><span></span></div>
  <div class="abs brand"><div class="brand-dot"></div><div class="brand-name">Sunlit Path Society</div></div>
  <div class="abs call">
    <svg width="26" height="26" viewBox="0 0 26 26" fill="none" stroke="#4d6b4c" stroke-width="1.6"><circle cx="13" cy="13" r="11.5"/><path d="M9 8c-1 2 0 6 4 9 2 1.5 3.5 1.6 4.5.6l-1.8-2-1.6.8c-1.3-.7-2.6-2-3.2-3.3l.8-1.5-2-1.8z"/></svg>
    <div><b>Call Us Now</b><br>(00) 555 010 220</div>
  </div>
</header>

<section>
  <svg class="abs hero" viewBox="0 0 1200 572" preserveAspectRatio="none" role="img" aria-label="Faded photo of a group of young people working together in a bright room">
    <defs><linearGradient id="heroBg" x1="0" y1="0" x2="1" y2="1"><stop offset="0" stop-color="#e9e6e2"/><stop offset=".5" stop-color="#f2f1ef"/><stop offset="1" stop-color="#d8d5d1"/></linearGradient></defs>
    <path d="M0 0H1200V530Q900 500 600 572Q300 520 0 530Z" fill="url(#heroBg)"/>
  </svg>
  <h1 class="abs heading hero-title">We Compensate Your<br>Carbon Footprint</h1>
  <p class="abs hero-text">Lorem Ipsum is simply dummy text of the printing and typesetting industry.</p>
  <div class="btn" style="left:128px;top:465px;width:177px;height:38px">Get A Free Quote</div>
  <div class="abs video" role="img" aria-label="Video still of a cheerful team gathered around a laptop"></div>
  <svg class="abs" style="left:834px;top:380px" width="54" height="54" viewBox="0 0 54 54" fill="none" stroke="#fff" stroke-width="2.5"><circle cx="27" cy="27" r="24"/><path d="M21 16l17 11-17 11z"/></svg>
  <div class="abs video-bar"></div><div class="abs video-knob"></div>
</section>

<section>
  <div class="step" style="left:69px">
    <div class="step-circle active"><svg width="110" height="110" viewBox="0 0 110 110" fill="none" stroke="#fff" stroke-width="4"><rect x="25" y="8" width="60" height="94" rx="10"/><rect x="36" y="20" width="38" height="12" rx="3"/><circle cx="42" cy="48" r="5"/><circle cx="55" cy="48" r="5"/><circle cx="68" cy="48" r="5"/><circle cx="42" cy="64" r="5"/><circle cx="55" cy="64" r="5"/><circle cx="68" cy="64" r="5"/><circle cx="42" cy="80" r="5"/><circle cx="55" cy="80" r="5"/><rect x="63" y="59" width="10" height="27" rx="5"/></svg></div>
    <h3>Calculate</h3><p>Lorem Ipsum is simply dummy a text of the printing and typeset ting industry</p>
  </div>
  <div class="step" style="left:285px">
    <div class="step-circle"><svg width="110" height="110" viewBox="0 0 110 110" fill="none" stroke="#fff" stroke-width="4"><circle cx="55" cy="55" r="34"/><circle cx="55" cy="55" r="14"/><path d="M55 8v32M55 70v32M8 55h32M70 55h32"/></svg></div>
    <h3>Aim</h3><p>Lorem Ipsum is simply dummy a text of the printing and typeset ting industry</p>
  </div>
  <div class="step" style="left:498px">
    <div class="step-circle"><svg width="110" height="110" viewBox="0 0 110 110" fill="none" stroke="#fff" stroke-width="4"><path d="M12 98h86M20 98V18h14l48 60"/><path d="M72 78h14V64"/><path d="M36 98V48M52 98V62M68 98V82"/></svg></div>
    <h3>Reduce</h3><p>Lorem Ipsum is simply dummy a text of the printing and typeset ting industry</p>
  </div>
  <div class="step" style="left:713px">
    <div class="step-circle"><svg width="110" height="110" viewBox="0 0 110 110" fill="none" stroke="#fff" stroke-width="4"><path d="M55 102V40M55 66l-12-12M55 58l12-10"/><path d="M55 82c-16 0-28-10-28-24 0-6 3-10 6-13-1-12 8-24 22-24s23 12 22 24c3 3 6 7 6 13 0 14-12 24-28 24z"/></svg></div>
    <h3>Offset</h3><p>Lorem Ipsum is simply dummy a text of the printing and typeset ting industry</p>
  </div>
  <div class="step" style="left:930px">
    <div class="step-circle"><svg width="110" height="110" viewBox="0 0 110 110" fill="none" stroke="#fff" stroke-width="4"><path d="M34 14h64v46H62L48 72V60H34z"/><path d="M26 36H12v46h14v14l14-14h34V68"/><path d="M48 30h36M48 44h24"/></svg></div>
    <h3>Communicate</h3><p>Lorem Ipsum is simply dummy a text of the printing and typeset ting industry</p>
  </div>
</section>

<section>
  <article class="project" style="left:82px">
    <div class="project-photo" role="img" aria-label="Volunteers planting a young tree in a park" style="background:linear-gradient(160deg,#9fb7c9,#6f9a55 55%,#3e5a2c)"></div>
    <h3>Tree Planting</h3><p>Lorem Ipsum is simply dummy the printing and typesetting industry. Lorem Ipsum has been the standard dummy.</p>
    <div class="btn">Read More</div>
  </article>
  <article class="project" style="left:440px">
    <div class="project-photo" role="img" aria-label="Hands around a seedling growing from dark soil" style="background:radial-gradient(circle at 50% 45%,#8c7a4e,#5a4936 45%,#2b2620)"></div>
    <h3>Forest Protection</h3><p>Lorem Ipsum is simply dummy the printing and typesetting industry. Lorem Ipsum has been the standard dummy.</p>
    <div class="btn">Read More</div>
  </article>
  <article class="project" style="left:796px">
    <div class="project-photo" role="img" aria-label="Wind turbines on a hill under a pale sky" style="background:linear-gradient(180deg,#b8bcb4,#a7ab9f 70%,#55603f)"></div>
    <h3>Carbon Credits</h3><p>Lorem Ipsum is simply dummy the printing and typesetting industry. Lorem Ipsum has been the standard dummy.</p>
    <div class="btn">Read More</div>
  </article>
</section>

<section>
  <svg class="abs offset" viewBox="0 0 1200 453" preserveAspectRatio="none" role="img" aria-label="Hand holding a smartphone showing a route map">
    <defs><linearGradient id="offBg" x1="0" y1="0" x2="1" y2="1"><stop offset="0" stop-color="#c9b9a3"/><stop offset=".5" stop-color="#e8e6e3"/><stop offset="1" stop-color="#cfc8bd"/></linearGradient></defs>
    <rect width="1200" height="453" fill="url(#offBg)"/>
    <path d="M0 0H480L270 453H0Z" fill="#79c69a"/>
  </svg>
  <div class="abs offset-box">
    <h2>Calculated Carbon footprint<br>and ready to offset?</h2>
    <p>Lorem Ipsum is simply dummy the printing and typesetting industry. Lorem Ipsum has been the standard dummy.</p>
    <div class="counter">
      <div class="group"><span class="digit">1</span><span class="digit">4</span></div>
      <div class="group"><span class="digit">5</span><span class="digit">3</span><span class="digit">7</span></div>
      <div class="group"><span class="digit">9</span><span class="digit">9</span><span class="digit">0</span></div>
      <span>KM</span>
    </div>
    <div class="btn light">Compensados</div>
  </div>
</section>

<section>
  <h2 class="abs heading news-title">Latest News</h2>
  <article class="news-card" style="left:70px">
    <div class="news-photo" role="img" aria-label="Young people talking in a bright lounge" style="background:linear-gradient(135deg,#d8d4cf,#8e8478 60%,#6a5a4c)"></div>
    <div class="news-date">11<br>Oct</div>
    <h4>What is Lorem Ipsum?</h4>
    <p>Lorem ipsum dolor sit amet, consectetur adipiscing elit, sed do eiusmod tempor incididunt ut labore et dolore magna aliqua.</p>
    <a href="#">Read More</a>
  </article>
  <article class="news-card" style="left:428px">
    <div class="news-photo" role="img" aria-label="Team meeting around a wooden table" style="background:linear-gradient(135deg,#a0624c,#c9b6a0 50%,#7d6b5c)"></div>
    <div class="news-date">11<br>Oct</div>
    <h4>What is Lorem Ipsum?</h4>
    <p>Lorem Ipsum is simply dummy the printing and typesetting industry. Lorem Ipsum has been the standard dummy.</p>
    <a href="#">Read More</a>
  </article>
  <article class="news-card" style="left:792px">
    <div class="news-photo" role="img" aria-label="Colleagues chatting with coffee in an office" style="background:linear-gradient(135deg,#5f7590,#d7d2cb 50%,#8a96a4)"></div>
    <div class="news-date">11<br>Oct</div>
    <h4>What is Lorem Ipsum?</h4>
    <p>Lorem Ipsum is simply dummy the printing and typesetting industry. Lorem Ipsum has been the standard dummy.</p>
    <a href="#">Read More</a>
  </article>
</section>

<section>
  <div class="abs benefit-block"></div>
  <div class="abs benefit-photo" role="img" aria-label="Sunlit park path lined with tall trees" style="background:linear-gradient(180deg,#c5d3b6,#7d9a55 50%,#4f7a26)"></div>
  <h2 class="abs heading benefit-title">How it Benefits us</h2>
  <div class="abs benefit-rule"></div>
  <p class="abs benefit-text">Lorem Ipsum is simply dummy text of the printing and typesetting industry. Lorem Ipsum has been the industry's standard dummy text ever since the 1500s, when an unknown printer took a galley of type and scrambled it to make a type specimen book. It has survived not only five centuries.</p>
  <ul class="abs checks">
    <li><svg width="16" height="16" viewBox="0 0 16 16" fill="none" stroke="#555" stroke-width="1.3"><circle cx="8" cy="8" r="7"/><path d="M4.5 8.2l2.4 2.3 4.6-5"/></svg>Lorem Ipsum is simply dummy text of the printing</li>
    <li><svg width="16" height="16" viewBox="0 0 16 16" fill="none" stroke="#555" stroke-width="1.3"><circle cx="8" cy="8" r="7"/><path d="M4.5 8.2l2.4 2.3 4.6-5"/></svg>Simply dummy text of the printing</li>
    <li><svg width="16" height="16" viewBox="0 0 16 16" fill="none" stroke="#555" stroke-width="1.3"><circle cx="8" cy="8" r="7"/><path d="M4.5 8.2l2.4 2.3 4.6-5"/></svg>Ipsum is simply dummy text of the printing</li>
  </ul>
  <div class="btn" style="left:609px;top:3117px;width:177px;height:38px">Read More</div>
</section>

<footer>
  <svg class="abs footer" viewBox="0 0 1200 275" preserveAspectRatio="none" role="img" aria-label="Dim city skyline behind the footer">
    <path d="M0 40L600 0L1200 40V275H0Z" fill="#4a4a4a"/>
  </svg>
  <div class="abs footer-brand"><div class="brand-dot"></div><div class="brand-name">Sunlit Path Society</div></div>
  <div class="abs socials"><span class="social on"></span><span class="social"></span><span class="social"></span><span class="social"></span></div>

  <div class="abs contact-title">Contact us</div>
  <div class="abs contact-rule"></div>
  <div class="field" style="left:402px;top:3372px;width:126px">Name</div>
  <div class="field" style="left:538px;top:3372px;width:124px">Phone</div>
  <div class="field" style="left:670px;top:3372px;width:126px">Email</div>
  <div class="field" style="left:402px;top:3412px;width:394px;height:58px">Message</div>
  <div class="btn light" style="left:521px;top:3478px;width:155px;height:34px;font-size:13px">Send</div>

  <div class="abs quick">
    <h5>Quick Contact</h5>
    <div class="quick-rule"></div>
    <ul>
      <li><span class="ic"><svg width="12" height="14" viewBox="0 0 12 14" fill="none" stroke="#fff"><path d="M6 13s5-5 5-8A5 5 0 001 5c0 3 5 8 5 8z"/><circle cx="6" cy="5" r="1.6"/></svg></span>48 Meadow Lane</li>
      <li><span class="ic"></span>Fernwood, ST 40210</li>
      <li><span class="ic"><svg width="14" height="12" viewBox="0 0 14 12" fill="none" stroke="#fff"><rect x="1" y="4" width="12" height="7" rx="1"/><path d="M3 4V1h8v3"/></svg></span>+00 555 010 2200</li>
      <li><span class="ic"><svg width="14" height="10" viewBox="0 0 14 10" fill="none" stroke="#fff"><rect x=".5" y=".5" width="13" height="9"/><path d="M.5.5L7 6l6.5-5.5"/></svg></span>hello@sunlitpath.org</li>
    </ul>
  </div>
  <p class="abs copyright">Copyright © 2019 Sunlit Path Society. All Right Reserve</p>
</footer>

</body>
</html>
```